ROSE WINE LABEL

WE NEED A LABEL DESIGN FOR A NEW ROSE WINE MADE IN MEXICO. THIS IS A NEW WINARY THAT WANTS TO DO SOMETHING DIFFERENT FOR THE WINE INDUSTRY IN MEXICO, EXCELENT QUALITY OF WINE ACCESIBLE FOR EVERYONE. WINE CULTURE IN MEXICO IS NOT GOOD, WE WANT TO INNOVATE IN THE MARKET, BRING WINE TO YOUNG PEOPLE WITHOUT MAKING IT SEAM LIKE A "LUXURY" PRODUCT, LET THEM KNOW THAT YOU CAN DRINK WINE EVERYDAY EVERYTIME, SOMETHING EASY TO ANALYZE, DRINK AND UNDERSTAND, SOMETHING TO LET KNOW THE CONSUMERS ABOUT THE GOOD QUALITY OF WINE YOU CAN FIND IN MEXICO. I WANT TO SEE A DIFFERENT DESIGN. WE WANT TO KEEP WORKING WITH THE DESIGNER FOR THE REST OF THE LABELS, AROUND 6-7. THE NAME OF THE WINARY IS "VINOS DEL ROBLEDAL" AND THE NAMES OF THE WINES ARE GOING TO HAVE THE "ROBLEDAL" AND THE DIFFERENT FINE ARTS LIKE PAINTING, DANCE, LITERATURE, ETC.
THE BOTTLE OF THIS WINE IS GOING TO BE REGULAR SHAPE ALSO KNOWN AS BODEAUX, TRANSPARENT AND LIGHT GREEN ALSO KNOWN AS "GREEN CHAMPAGNE", SILVER & BLACK CAPSULE.

Requirements
Must have
• THE LABEL MUST HAVE THE NAME OF THE WINE "BAILE DE LA ROBLEDANA" AND IN A SMALLER FONT "QUERÉTARO, MÉXICO"
Nice to have
• A COLORFUL AND MODERN DESIGN, I AM ATTACHING THE LOGO OF THE WINARY. IT IS NOT NECESARY TO ADD IT TO THE LABEL, BUT PERHAPS SOMEONE IS INTERESTED IN THE "VR" OF THE DESIGN FROM INSIDE THE SHELL.
Should not have
• THE DESIGN SHOULD BE ABLE TO FIT IN A REGULAR FORM, RECTANGULAR, SQUARE, OR CIRCLE, NO SPECIAL DIE CUTTING CAN BE MADE TO THE LABEL.

```html
<!DOCTYPE html>
<html lang="es">
<head>
<meta charset="utf-8">
<title>Baile de la Robledana – Rosé 2013</title>
<link href="https://fonts.googleapis.com/css2?family=Pinyon+Script&family=Oswald:wght@300&family=Tinos&display=swap" rel="stylesheet">
<style>
  :root {
    --label-pink: #f98ca8;
    --mark-pink: #fca2bb;
    --dress-crimson: #d8123f;
    --dress-deep: #b0062e;
    --dress-rose: #ec3d68;
    --title-white: #ffffff;
    --origin-navy: #1c1a8f;
    --vintage-navy: #1b2299;
    --variety-coral: #f24f70;
    --fine-print: #ffffff;
  }
  * { margin: 0; padding: 0; box-sizing: border-box; }
  html, body { width: 1050px; height: 1200px; overflow: hidden; background: var(--label-pink); }
  .label {
    position: relative;
    width: 1050px;
    height: 1200px;
    background: var(--label-pink);
    overflow: hidden;
  }
  .winery-mark {
    position: absolute;
    left: 560px;
    top: 300px;
    width: 440px;
    text-align: center;
    white-space: nowrap;
    font-family: 'Tinos', serif;
    font-size: 28px;
    letter-spacing: 5px;
    color: var(--mark-pink);
  }
  .dancer-art {
    position: absolute;
    left: 0;
    top: 0;
    width: 700px;
    height: 1200px;
  }
  .wine-name {
    position: absolute;
    inset: 0;
    font-family: 'Pinyon Script', cursive;
    color: var(--title-white);
    font-weight: 400;
  }
  .wine-name span { position: absolute; white-space: nowrap; line-height: 1; }
  .wine-name .word-baile { left: 60px; top: 440px; font-size: 160px; }
  .wine-name .word-de-la { left: 175px; top: 630px; font-size: 84px; }
  .wine-name .word-robledana { left: 345px; top: 548px; font-size: 160px; }
  .origin {
    position: absolute;
    left: 597px;
    top: 744px;
    font-family: 'Tinos', serif;
    font-size: 31px;
    color: var(--origin-navy);
    letter-spacing: 0.5px;
  }
  .variety {
    position: absolute;
    left: 716px;
    top: 1009px;
    font-family: 'Oswald', sans-serif;
    font-weight: 300;
    font-size: 142px;
    line-height: 1;
    color: var(--variety-coral);
    letter-spacing: 2px;
    white-space: nowrap;
    transform: scaleX(0.74);
    transform-origin: left top;
  }
  .vintage {
    position: absolute;
    left: 969px;
    top: 1087px;
    transform: translate(-50%, -50%) rotate(90deg) scaleX(0.8);
    font-family: 'Oswald', sans-serif;
    font-weight: 300;
    font-size: 96px;
    line-height: 1;
    color: var(--vintage-navy);
    white-space: nowrap;
  }
  .alcohol {
    position: absolute;
    left: 14px;
    top: 1173px;
    font-family: 'Oswald', sans-serif;
    font-weight: 300;
    font-size: 11px;
    color: var(--fine-print);
  }
</style>
</head>
<body>
<main class="label">
  <div class="winery-mark">VINOS DEL ROBLEDAL</div>

  <svg class="dancer-art" role="img" aria-label="Watercolour illustration of a flamenco dancer in a sweeping crimson ruffled dress" viewBox="0 0 700 1200">
    <defs>
      <radialGradient id="dress-glow" cx="0.35" cy="0.62" r="0.7">
        <stop offset="0" stop-color="var(--dress-deep)"/>
        <stop offset="0.45" stop-color="var(--dress-crimson)"/>
        <stop offset="0.8" stop-color="var(--dress-rose)"/>
        <stop offset="1" stop-color="var(--label-pink)" stop-opacity="0"/>
      </radialGradient>
    </defs>
    <path d="M0 170 C120 60 300 60 370 140 C390 330 420 470 470 520 C560 640 680 820 640 1000 C560 1100 400 1200 250 1200 L0 1200 Z" fill="url(#dress-glow)"/>
  </svg>

  <h1 class="wine-name">
    <span class="word-baile">Baile</span>
    <span class="word-de-la">de la</span>
    <span class="word-robledana">Robledana</span>
  </h1>

  <p class="origin">QUERÉTARO, MÉXICO</p>

  <p class="variety">ROSE</p>
  <p class="vintage">2013</p>

  <p class="alcohol">ALC. 14.5% By VOL</p>
</main>
</body>
</html>
```